Ravelor Global Kft. is an online recruitment marketplace connecting the employers and recruiters together. We provide an e-bussiness solution for companies and give busines opportunity for recruiters.
We have a logo design already, which should be used on the business card.
Our colours are grey and magenta, which can be seen in the logo. Black is also welcome.
The style should be dynamic, young but professional. It should be clear, visible, elegant, not too crowded, simple but exciting.
We need the following data on the BC: name, title, address, phone,fax and mobile number, email address, website.
Target Market(s)
Our target market are companies, as this is a B2B business. We also target recruiters, recruitment professionals, headhunters.We would like to be impressive and different.
Industry/Entity Type
Business
Requirements
Must have
- We would like to promote our website, www.ravelorglb.hu.
- Please, put this on the back with a quite visible letter size.The style should be dynamic, young but professional. It should be clear, visible, elegant, not too crowded, simple but exciting.
Should not have
- We do not want to see people figures.

```html
<!DOCTYPE html>
<html lang="en">
<head>
<meta charset="utf-8">
<title>Ravelor Global Kft. – Business Card</title>
<link href="https://fonts.googleapis.com/css2?family=Arimo:wght@400;700&family=Archivo+Narrow:wght@400;700&display=swap" rel="stylesheet">
<style>
  :root {
    --magenta: #c01f73;
    --mauve: #86737f;
    --band-grey: #d4d4d4;
    --ink: #000000;
    --paper: #ffffff;
  }
  * { margin: 0; padding: 0; box-sizing: border-box; }
  html, body {
    width: 1200px;
    height: 662px;
    overflow: hidden;
    background: var(--paper);
  }
  .card {
    position: relative;
    width: 1200px;
    height: 662px;
    background: var(--paper);
    overflow: hidden;
  }
  .brand-band {
    position: absolute;
    left: 935px;
    top: 0;
    width: 196px;
    height: 662px;
    background: var(--band-grey);
  }
  .identity {
    position: absolute;
    left: 2px;
    top: 68px;
  }
  .identity__name {
    font-family: "Arimo", Arial, sans-serif;
    font-weight: 700;
    font-size: 41px;
    line-height: 46px;
    color: var(--ink);
  }
  .identity__title {
    font-family: "Archivo Narrow", "Arial Narrow", sans-serif;
    font-weight: 400;
    font-size: 29px;
    line-height: 32px;
    color: var(--mauve);
  }
  .contact {
    position: absolute;
    left: 1px;
    top: 374px;
    font-style: normal;
    font-family: "Archivo Narrow", "Arial Narrow", sans-serif;
    font-size: 29px;
    line-height: 32.4px;
    color: var(--ink);
  }
  .contact__row {
    display: flex;
    white-space: nowrap;
  }
  .contact__label {
    font-family: "Arimo", Arial, sans-serif;
    font-weight: 700;
    font-size: 27px;
    color: var(--magenta);
    width: 120px;
    flex: none;
    display: flex;
    justify-content: space-between;
    padding-right: 10px;
  }
  .brand {
    position: absolute;
    left: 778px;
    top: 330px;
    width: 204px;
  }
  .brand__name {
    font-family: "Arimo", Arial, sans-serif;
    font-weight: 700;
    font-size: 40px;
    line-height: 48px;
    color: var(--magenta);
    white-space: nowrap;
  }
  .brand__square {
    position: absolute;
    left: 778px;
    top: 398px;
    width: 204px;
    height: 197px;
    background: var(--mauve);
  }
</style>
</head>
<body>
  <main class="card">
    <div class="brand-band"></div>

    <header class="identity">
      <h1 class="identity__name">Daniel Varkonyi</h1>
      <p class="identity__title">Managing Director</p>
    </header>

    <address class="contact">
      <div class="contact__row">412 Lindell Avenue North</div>
      <div class="contact__row">Brantwick, Ontario, K7R 2M4</div>
      <div class="contact__row"><span class="contact__label"><span>phone</span><span>:</span></span><span>555.204-3318</span></div>
      <div class="contact__row"><span class="contact__label"><span>mob</span><span>:</span></span><span>555.719.2046</span></div>
      <div class="contact__row"><span class="contact__label"><span>fax</span><span>:</span></span><span>555-204-3319</span></div>
      <div class="contact__row"><span class="contact__label"><span>email</span><span>:</span></span><span>daniel@ravelorglb.hu</span></div>
      <div class="contact__row"><span class="contact__label"><span>web</span><span>:</span></span><span>www.ravelorglb.hu</span></div>
    </address>

    <div class="brand">
      <p class="brand__name">Ravelor</p>
    </div>
    <div class="brand__square" aria-hidden="true"></div>
  </main>
</body>
</html>
```